Book Cover Design Project

Title : "Lantern Ridge" - A non builders guide to the commercial building process
This is a business book aimed at those who have never been through the commercial construction process. It contains some project management techniques and and holds the readers hands through the development and building steps. It explains details on different concepts and informs the reader on behind the scenes in the industry. The typical project ranges from 500k to 3 Million.
Assume a design size around A5
Back cover must have:
ISBN and bar code
Area for Synopisis
Area for my profile / photo
Its generally a business book, but professionals looks for ideas in project management and other concepts may find it usefull
Construction

```html
<!DOCTYPE html>
<html lang="en">
<head>
<meta charset="utf-8">
<title>Lantern Ridge — Book Cover</title>
<link rel="stylesheet" href="https://fonts.googleapis.com/css2?family=Anton&family=Oswald:wght@500;700&display=swap">
<style>
  :root {
    --page-bg: #ffffff;
    --sky-top: #6f93c4;
    --sky-cloud: #dfe7f1;
    --city-dark: #5d6f86;
    --city-mid: #8fa0b4;
    --city-light: #c3cdd8;
    --haze: #f7f6fb;
    --room-light: #d6d3ec;
    --room-mid: #8b84c2;
    --room-deep: #3b3c84;
    --title-top: #a4a8da;
    --title-bottom: #3f4a9a;
    --subtitle: #2e3a6c;
    --accent-red: #d6262b;
  }
  * { margin: 0; padding: 0; box-sizing: border-box; }
  html, body { width: 802px; height: 1200px; overflow: hidden; background: var(--page-bg); }
  .cover {
    position: relative;
    width: 802px;
    height: 1200px;
    overflow: hidden;
    background: var(--page-bg);
  }
  .cover__photo {
    position: absolute;
    inset: 0;
    background:
      radial-gradient(ellipse 60% 8% at 70% 6%, rgba(255,255,255,0.75) 0%, rgba(255,255,255,0) 100%),
      radial-gradient(ellipse 45% 6% at 20% 10%, rgba(255,255,255,0.6) 0%, rgba(255,255,255,0) 100%),
      radial-gradient(ellipse 70% 14% at 50% 43%, var(--haze) 0%, rgba(247,246,251,0) 100%),
      radial-gradient(ellipse 75% 22% at 50% 58%, var(--room-light) 0%, rgba(214,211,236,0) 100%),
      linear-gradient(180deg,
        var(--sky-top) 0%,
        var(--sky-cloud) 11%,
        var(--city-mid) 17%,
        var(--city-dark) 24%,
        var(--city-mid) 31%,
        var(--city-dark) 36%,
        var(--city-light) 41%,
        var(--haze) 45%,
        var(--room-light) 54%,
        var(--room-mid) 76%,
        var(--room-deep) 100%);
  }
  .cover__title {
    position: absolute;
    left: 0; right: 0;
    top: 505px;
    text-align: center;
    font-family: "Anton", "Oswald", sans-serif;
    font-weight: 400;
    text-transform: uppercase;
    line-height: 0.9;
  }
  .title__word {
    display: block;
    background: linear-gradient(180deg, var(--title-top) 0%, var(--title-bottom) 100%);
    -webkit-background-clip: text;
    background-clip: text;
    color: transparent;
  }
  .title__word--small { font-size: 84px; letter-spacing: 2px; }
  .title__word--large { font-size: 200px; letter-spacing: 4px; margin-top: -4px; }
  .cover__subtitle {
    position: absolute;
    left: 0; right: 0;
    top: 790px;
    text-align: center;
    text-transform: uppercase;
  }
  .subtitle__lead {
    display: block;
    font-family: "Oswald", sans-serif;
    font-weight: 700;
    font-size: 34px;
    letter-spacing: 1px;
    color: var(--subtitle);
  }
  .subtitle__main {
    display: block;
    font-family: "Anton", sans-serif;
    font-size: 100px;
    line-height: 1.04;
    color: var(--accent-red);
    letter-spacing: 2px;
  }
</style>
</head>
<body>
  <main class="cover">
    <div class="cover__photo" role="img" aria-label="Photograph of a dense city skyline under a pale blue sky, fading into a glossy boardroom table with office chairs in violet-blue light"></div>

    <h1 class="cover__title">
      <span class="title__word title__word--small">Lantern</span>
      <span class="title__word title__word--large">Ridge</span>
    </h1>

    <p class="cover__subtitle">
      <span class="subtitle__lead">A non builders guide to the</span>
      <span class="subtitle__main">Commercial</span>
      <span class="subtitle__main">Building Process</span>
    </p>
  </main>
</body>
</html>
```